NovaLUX.academy

design a responsive website in WordPress. I've purchased the Ferno theme - it would be nice to use, but not necessary.Blog - needs to display/filter multiple categories. Preferably color coded.Podcasts - same as blog.Learn - something like qlimo.org. User's need to subscribe to courses (free & paid). Each course will have multiple modules, documents and quizzes. Users will be granted a "certificate" open successful competition. Store - About Us - Why We are Doing this, Team Members Bios, etc.Contact Us -

Target Market(s)

everyone that uses tech

Industry/Entity Type

Tech

Number of Pages Required

5+ page

Font styles to use
Sans Serif

Requirements
Must have
• Wordpress
• responsive
• Learn, Blog, Podcasts, Store, About Us, Contact Us
Nice to have
• Ferno Theme

```html
<!DOCTYPE html>
<html lang="en">
<head>
<meta charset="utf-8">
<title>NovaLUX.academy</title>
<link href="https://fonts.googleapis.com/css2?family=Montserrat:wght@400;500;600;700&family=Open+Sans:wght@400;600&display=swap" rel="stylesheet">
<style>
:root{
  --orange:#f26b1d;
  --blue:#1b9bd7;
  --blue-dark:#1e86c0;
  --navy:#1f2a44;
  --text:#555b66;
  --light-gray:#f1f1f1;
  --light-blue:#e4f1f6;
  --tag-red:#e8253f;
  --tag-sky:#4ec3e0;
  --tag-blue:#3b8fd6;
  --tag-teal:#1a9b8c;
  --tag-pink:#e0267d;
  --tag-orange:#f57f1f;
  --dark:#333;
}
*{margin:0;padding:0;box-sizing:border-box}
html,body{width:1200px;height:4327px;overflow:hidden}
body{position:relative;background:#fff;font-family:"Open Sans",sans-serif;color:var(--text)}
.abs{position:absolute}
.heading{font-family:"Montserrat",sans-serif;font-weight:500;text-align:center}
.center{left:0;width:1200px;text-align:center}

/* header */
.logo{display:flex;align-items:center;gap:10px;font-family:"Montserrat",sans-serif;font-weight:600;color:var(--blue);font-size:26px}
.logo .dot{width:26px;height:26px;border-radius:50%;background:var(--orange)}
.topbar{right:66px;top:20px;display:flex;align-items:center;gap:8px;font-size:13px}
.cart{background:var(--orange);color:#fff;padding:10px 14px;font-family:"Montserrat",sans-serif;font-weight:600;font-size:12px;border-radius:2px}
.nav{top:78px;right:66px;display:flex;gap:38px;font-family:"Montserrat",sans-serif;font-size:13px;font-weight:500;color:var(--navy)}
.nav .active{color:var(--blue)}

/* hero */
.hero-art{left:500px;top:120px;width:640px;height:740px;border-radius:24px;background:radial-gradient(circle at 60% 40%,#3b4b6a 0%,#6f87a8 35%,#dfe7ee 70%,#f4f6f8 100%)}
.hero-title{left:110px;top:332px;font-family:"Montserrat",sans-serif;font-size:50px;color:var(--blue);font-weight:500}
.hero-text{left:112px;top:420px;width:390px;font-size:12.5px;line-height:27px}
.btn{display:inline-block;font-family:"Montserrat",sans-serif;font-weight:600;color:#fff;border-radius:30px;text-align:center}
.hero-btn{left:112px;top:562px;width:288px;height:58px;line-height:58px;background:var(--orange);font-size:15px}
.bubble{border-radius:50%;background:#e6e6e6}
.photo{border-radius:50%}

/* elements */
.el-title{top:886px;font-size:36px;color:var(--blue)}
.el-sub{top:936px;font-size:28px;color:var(--orange);font-weight:400}
.el-text{top:1004px;left:255px;width:690px;text-align:center;font-size:13px;line-height:28px}
.pill{display:flex;gap:8px;left:405px;top:1205px}
.pill .item{width:124px;text-align:center}
.pill .ring{width:96px;height:96px;border-radius:50%;margin:0 auto;display:flex;align-items:center;justify-content:center}
.pill .bar{height:12px;margin-top:-30px;border-radius:6px}
.pill .label{font-family:"Montserrat",sans-serif;font-weight:600;font-size:14px;margin-top:28px}

/* courses */
.courses-bg{left:0;top:1366px;width:1200px;height:600px;background:var(--light-gray)}
.sec-title{font-size:40px;color:var(--blue)}
.sec-intro{left:200px;width:800px;font-size:12px;line-height:26px;text-align:center}
.card{top:1538px;width:228px;height:314px;background:#fff;text-align:center;padding-top:28px;box-shadow:0 0 6px rgba(0,0,0,.06)}
.card h3{font-family:"Montserrat",sans-serif;font-weight:500;font-size:17px;color:var(--blue);margin:20px 0 14px}
.card p{font-size:11.5px;line-height:22px;padding:0 22px}
.card .take{display:inline-block;margin-top:18px;border:1.5px solid var(--blue);color:var(--blue);border-radius:20px;padding:10px 14px;font-family:"Montserrat",sans-serif;font-weight:600;font-size:11px}
.card.featured{background:var(--orange);border:4px solid var(--blue)}
.card.featured h3,.card.featured p{color:#fff}
.card.featured .take{border-color:#fff;color:#fff}
.dots{top:1883px;left:572px;display:flex;gap:4px}
.dots span{width:14px;height:14px;border-radius:50%;border:2px solid #bbb}

/* tags */
.tags{display:flex;gap:6px;left:0;width:1200px;justify-content:center}
.tag{color:#fff;font-family:"Montserrat",sans-serif;font-weight:500;font-size:15px;padding:0 22px;height:36px;line-height:36px;border-radius:18px}

/* blog */
.blog-card{top:2288px;width:306px;height:395px;background:#fff;text-align:center;padding-top:175px}
.blog-card h3{font-family:"Montserrat",sans-serif;font-weight:500;font-size:25px;color:var(--dark)}
.blog-card p{font-size:15px;line-height:24px;padding:10px 40px 0;color:#333}
.plus{display:inline-block;width:34px;height:34px;border-radius:50%;background:var(--orange);color:#fff;line-height:34px;font-weight:700;margin-top:16px}
.blog-photo{top:2220px;width:237px;height:237px;border:4px solid var(--blue);border-radius:50%}

/* podcast */
.pod-title{left:600px;top:3240px;width:486px;font-family:"Montserrat",sans-serif;font-weight:600;font-size:25px;color:var(--dark);text-align:center}
.pod-text{left:648px;top:3298px;width:390px;font-size:13px;line-height:26px;text-align:center}
.player{left:594px;top:3512px;width:462px;height:72px;background:#eef0f2;border-radius:36px}

/* newsletter */
.news{left:0;top:3660px;width:1200px;height:345px;background:var(--blue-dark);color:#fff}
.news h2{position:absolute;top:46px;width:100%;text-align:center;font-family:"Montserrat",sans-serif;font-weight:500;font-size:38px}
.news p{position:absolute;left:250px;top:112px;width:700px;text-align:center;font-size:12.5px;line-height:28px;color:#d9ecf7}
.news .input{position:absolute;left:251px;top:191px;width:695px;height:49px;background:#fff;color:#888;font-size:12px;line-height:49px;padding-left:20px}
.news .subscribe{position:absolute;left:502px;top:258px;width:193px;height:44px;line-height:44px;background:var(--orange);font-size:15px;border-radius:4px}

/* footer */
.footer-line{left:112px;top:4163px;width:976px;height:1px;background:#e0e0e0}
.social{left:390px;top:4180px;display:flex;gap:12px}
.social span{width:60px;height:60px;border-radius:50%;border:1.5px solid #ccc;display:flex;align-items:center;justify-content:center}
.social span i{width:10px;height:10px;border-radius:50%;background:#7b8494}
.copy{top:4272px;font-size:12px;color:#555}
</style>
</head>
<body>

<!-- header -->
<div class="abs logo" style="left:112px;top:40px"><span class="dot"></span>NovaLUX.academy</div>
<div class="abs topbar">
  <svg width="14" height="11" viewBox="0 0 14 11"><rect x="0.5" y="0.5" width="13" height="10" fill="none" stroke="#555"/><path d="M0.5 0.5 7 6 13.5 0.5" fill="none" stroke="#555"/></svg>
  <span>hello@novalux.academy</span>
  <span class="cart">0 ITEMS</span>
</div>
<nav class="abs nav"><span class="active">HOME</span><span>LEARN</span><span>BLOG</span><span>PODCASTS</span><span>STORE</span><span>ABOUT US</span><span>CONTACT US</span></nav>

<!-- hero -->
<div class="abs hero-art" role="img" aria-label="Technology illustration: circuit board, glowing app icons and a city skyline seen through magnifying lenses"></div>
<div class="abs hero-title">Enroll Today</div>
<div class="abs hero-text">Curabitur arcu erat, accumsan id imperdiet et, porttitor at sem. Cras ultricies ligula sed dictum porta. Lorem ipsum dolor sit amet, consectetur adipiscing elit. Curabitur non nulla sit amet nisl tempus convallis quis ac lectus. Curabitur arcu erat, accumsan id imperdiet et.</div>
<div class="abs btn hero-btn">Enrol in NovaLUX For Just $69</div>

<!-- digital elements -->
<div class="abs heading center el-title">DIGITAL ELEMENTS</div>
<div class="abs heading center el-sub">EVERYTHING YOU NEED TO KNOW ABOUT DIGITAL</div>
<div class="abs el-text">Technology is all around us, from the smart phones, to smart devices like watches and activity trackers – cameras and microphones are more common than coffee shops.But how much do we actually know about what our tech is tracking – and where does that data go?<br><br>NovaLUX Academy is here to raise awareness and educate, so that we can take advantage of technology to improve our lives and transform into the digital world – NovaLUX.</div>
<div class="abs pill">
  <div class="item">
    <div class="ring" style="border:9px solid var(--blue)"><svg width="36" height="40"><rect x="6" y="4" width="24" height="32" fill="none" stroke="var(--blue)" stroke-width="3"/><line x1="11" y1="14" x2="25" y2="14" stroke="var(--blue)" stroke-width="2"/><line x1="11" y1="21" x2="25" y2="21" stroke="var(--blue)" stroke-width="2"/></svg></div>
    <div class="bar" style="background:var(--blue)"></div>
    <div class="label" style="color:var(--blue)">LEARN</div>
  </div>
  <div class="item">
    <div class="ring" style="border:9px solid var(--orange)"><svg width="40" height="36"><rect x="4" y="8" width="32" height="24" fill="none" stroke="var(--orange)" stroke-width="3"/><rect x="14" y="3" width="12" height="6" fill="none" stroke="var(--orange)" stroke-width="2"/></svg></div>
    <div class="bar" style="background:var(--orange)"></div>
    <div class="label" style="color:var(--orange)">EXPERIENCE</div>
  </div>
  <div class="item">
    <div class="ring" style="border:9px solid #333"><svg width="40" height="40"><path d="M20 4V36M4 20H36M20 4l-5 5M20 4l5 5M20 36l-5-5M20 36l5-5M4 20l5-5M4 20l5 5M36 20l-5-5M36 20l-5 5" stroke="#333" stroke-width="2.5" fill="none"/></svg></div>
    <div class="bar" style="background:#333"></div>
    <div class="label" style="color:#333">TRANSFORM</div>
  </div>
</div>

<!-- courses -->
<div class="abs courses-bg"></div>
<div class="abs bubble" style="left:1085px;top:1410px;width:100px;height:100px;background:#e5e5e5"></div>
<div class="abs bubble" style="left:20px;top:1380px;width:70px;height:70px;background:#e8e8e8"></div>
<div class="abs heading center sec-title" style="top:1394px">Our Courses</div>
<div class="abs sec-intro" style="top:1446px;left:270px;width:660px">Class aptent taciti sociosqu ad litora torquent per conubia nostra, per inceptos himenaeos. Sed molestie, velit ut eleifend sollicitudin, neque orci tempor nulla, id sagittis nisl ante nec arcu.</div>

<div class="abs card" style="left:112px">
  <svg width="60" height="74"><ellipse cx="30" cy="40" rx="22" ry="7" fill="none" stroke="var(--blue)" stroke-width="3"/><path d="M8 40v18c0 4 10 7 22 7s22-3 22-7V40" fill="none" stroke="var(--blue)" stroke-width="3"/><line x1="30" y1="4" x2="30" y2="30" stroke="var(--blue)" stroke-width="3"/></svg>
  <h3>Data - Who owns it?</h3>
  <p>Duis egestas aliquet aliquet. Maecenas erat eros, fringilla et leo eget, orci dui tempor, dapibus nisi.</p>
  <span class="take">TAKE COURSE</span>
</div>
<div class="abs card featured" style="left:363px">
  <svg width="70" height="74"><path d="M35 4 64 20V54L35 70 6 54V20Z" fill="none" stroke="#fff" stroke-width="3"/><path d="M35 22 50 30V46L35 54 20 46V30Z" fill="#fff"/></svg>
  <h3>Python</h3>
  <p>Duis egestas aliquet aliquet. Maecenas erat eros, fringilla et leo eget, orci dui tempor, dapibus nisi.</p>
  <span class="take">TAKE COURSE</span>
</div>
<div class="abs card" style="left:612px">
  <svg width="78" height="74"><rect x="6" y="8" width="66" height="56" fill="none" stroke="var(--blue)" stroke-width="3"/><line x1="6" y1="18" x2="72" y2="18" stroke="var(--blue)" stroke-width="3"/><path d="M28 32l-8 9 8 9M50 32l8 9-8 9M43 30l-8 24" fill="none" stroke="var(--blue)" stroke-width="3"/></svg>
  <h3>HTML &amp; CSS</h3>
  <p>Duis egestas aliquet aliquet. Maecenas erat eros, fringilla et leo eget, orci dui tempor, dapibus nisi.</p>
  <span class="take">TAKE COURSE</span>
</div>
<div class="abs card" style="left:857px">
  <svg width="60" height="74"><rect x="10" y="6" width="14" height="62" fill="none" stroke="var(--blue)" stroke-width="3"/><path d="M38 20h12v48H38zM38 20l6-14 6 14" fill="none" stroke="var(--blue)" stroke-width="3"/></svg>
  <h3>UX Design</h3>
  <p>Duis egestas aliquet aliquet. Maecenas erat eros, fringilla et leo eget, orci dui tempor, dapibus nisi.</p>
  <span class="take">TAKE COURSE</span>
</div>
<div class="abs dots"><span></span><span></span><span></span></div>

<!-- blog -->
<svg class="abs" style="left:0;top:1966px" width="1200" height="930" aria-hidden="true"><path d="M0 150Q600 -20 1200 150V760Q600 1000 0 760Z" fill="var(--light-blue)"/></svg>
<div class="abs heading center sec-title" style="top:2006px">Latest Blog</div>
<div class="abs sec-intro" style="top:2066px">Curabitur arcu erat, accumsan id imperdiet et, porttitor at sem. Cras ultricies ligula sed dictum porta. Lorem ipsum dolor</div>
<div class="abs tags" style="top:2133px">
  <span class="tag" style="background:var(--tag-red)">GADGETS</span><span class="tag" style="background:var(--tag-sky)">SMART HOME</span><span class="tag" style="background:var(--tag-blue)">COOK BOOK</span><span class="tag" style="background:var(--tag-teal)">HTML &amp; CSS</span><span class="tag" style="background:var(--tag-pink)">UX DESIGN</span><span class="tag" style="background:var(--tag-orange)">OTHER</span>
</div>
<div class="abs blog-card" style="left:107px"><h3>BEST TABLET APPS</h3><p>To make your important health information accessible in case of emergencies, you can personalize your Medical ID on your handset.</p><span class="plus">+</span></div>
<div class="abs blog-card" style="left:438px"><h3>BEST TABLET APPS</h3><p>To make your important health information accessible in case of emergencies, you can personalize your Medical ID on your handset.</p><span class="plus">+</span></div>
<div class="abs blog-card" style="left:773px"><h3>BEST TABLET APPS</h3><p>To make your important health information accessible in case of emergencies, you can personalize your Medical ID on your handset.</p><span class="plus">+</span></div>
<div class="abs blog-photo" role="img" aria-label="Students studying in a classroom" style="left:142px;background:linear-gradient(135deg,#c89a74,#7a5a44)"></div>
<div class="abs blog-photo" role="img" aria-label="Hands working with a tablet and papers" style="left:473px;background:linear-gradient(135deg,#d8d2cc,#8a7f78)"></div>
<div class="abs blog-photo" role="img" aria-label="Person using a laptop" style="left:808px;background:linear-gradient(135deg,#dfe3e6,#6d6a68)"></div>
<div class="abs btn" style="left:487px;top:2748px;width:212px;height:40px;line-height:40px;background:var(--orange);font-size:13px">VIEW MORE POSTS</div>

<!-- podcasts -->
<div class="abs heading center sec-title" style="top:2924px;color:var(--orange)">Our Podcasts</div>
<div class="abs sec-intro" style="top:2984px">Curabitur arcu erat, accumsan id imperdiet et, porttitor at sem. Cras ultricies ligula sed dictum porta. Lorem ipsum dolor</div>
<div class="abs tags" style="top:3050px">
  <span class="tag" style="background:var(--tag-red)">GADGETS</span><span class="tag" style="background:var(--tag-sky)">SMART HOME</span><span class="tag" style="background:var(--tag-blue)">COOK BOOK</span><span class="tag" style="background:var(--tag-teal)">HTML &amp; CSS</span><span class="tag" style="background:var(--tag-pink)">UX DESIGN</span><span class="tag" style="background:var(--tag-orange)">OTHER</span>
</div>
<div class="abs photo" role="img" aria-label="Podcast host at a laptop" style="left:138px;top:3168px;width:404px;height:404px;background:linear-gradient(135deg,#e8ecef,#9aa7b2)"></div>
<svg class="abs" style="left:305px;top:3320px" width="86" height="86" aria-hidden="true"><circle cx="43" cy="43" r="40" fill="rgba(255,255,255,.2)" stroke="#fff" stroke-width="3"/><path d="M34 28 58 43 34 58Z" fill="#fff"/></svg>
<div class="abs photo" style="left:410px;top:3136px;width:216px;height:216px;background:var(--tag-pink);color:#fff;font-family:'Montserrat',sans-serif;font-weight:600;font-size:25px;text-align:center;line-height:216px">UX DESIGN</div>
<div class="abs pod-title">LOREM IPSUM PASSAGE</div>
<div class="abs pod-text">Duis egestas aliquet aliquet. Maecenas erat eros, fringilla et leo eget, viverra pretium nulla. Quisque sed augue tincidunt, posuere dui tempor, dapibus nisi. Donec vel lectus.Duis egestas aliquet aliquet. Maecenas erat eros, fringilla et leo eget, viverra pretium nulla. Quisque sed augue tincidunt, posuere dui tempor, dapibus nisi. Donec vel lectus.Sed ut perspiciatis unde omnis iste natus dolorinque laudantium, totam rem aperiam.</div>
<div class="abs player">
  <svg width="462" height="72" aria-hidden="true"><circle cx="42" cy="36" r="15" fill="var(--tag-red)"/><path d="M38 29 48 36 38 43Z" fill="#fff"/><line x1="70" y1="36" x2="400" y2="36" stroke="#c9ccd0" stroke-width="3"/><line x1="70" y1="36" x2="145" y2="36" stroke="var(--tag-red)" stroke-width="3"/><rect x="422" y="28" width="4" height="16" fill="#333"/><rect x="430" y="28" width="4" height="16" fill="#333"/></svg>
</div>

<!-- newsletter -->
<section class="abs news">
  <h2>Join Our Newsletter</h2>
  <p>Sed ut perspiciatis unde omnis iste natus error sit voluptatem accusantium doloremque laudantium, totam rem aperiam, eaque ipsa quae ab illo inventore veritatis et quasi architecto beatae vitae dicta sunt explicabo.</p>
  <div class="input">Enter You Email Id</div>
  <div class="btn subscribe">SUBSCRIBE</div>
</section>

<!-- footer -->
<div class="abs logo" style="left:480px;top:4070px;font-size:30px"><span class="dot" style="width:30px;height:30px"></span>NovaLUX.academy</div>
<div class="abs footer-line"></div>
<div class="abs social"><span><i></i></span><span><i></i></span><span><i></i></span><span><i></i></span><span><i></i></span><span><i></i></span></div>
<div class="abs center copy">© Copyrights 2018 - NovaLUX Academy All Rights Reserved</div>

</body>
</html>
```